Manufacturing company needs new business card.

I need a unique Business Card that will truly stand out. Nothing too busy. Simple is good, right? Not looking for a standard design either. No cookie cutter layout. I am just looking for something interesting and a bit different. Does't have to completely off the wall crazy, just not your run of the mill business card. Clean and modern with a touch of industrial.

Target Market(s)

Air conditioning industry, Architects, builders.

Industry/Entity Type

Business

Contact Information for Business Card

Details to be included on card are:

Peter Walsh
Managing Director

T: 1300 418 592
M: 0427 385 914
W: www.brandvalefabrication.com.au
E: peter.walsh@brandvalefabrication.com.au
A: 58 Harlow Lane, Sydney NSW 2000

Font styles to use
Sans Serif

Colors
0355a3
848484
fbfbfb

Requirements
Must have
• Card design must be landscape.

```html
<!DOCTYPE html>
<html lang="en">
<head>
<meta charset="utf-8">
<title>Brandvale Fabrication – Business Card</title>
<link href="https://fonts.googleapis.com/css2?family=Open+Sans:wght@400;600&display=swap" rel="stylesheet">
<style>
  :root {
    --brand-blue: #1f4fa6;
    --brand-blue-deep: #0355a3;
    --steel-grey: #848484;
    --paper: #fbfbfb;
    --ink: #2b2b2b;
    --backdrop: #e6e7ea;
  }
  * { margin: 0; padding: 0; box-sizing: border-box; }
  html, body { width: 1200px; height: 1000px; overflow: hidden; }
  body {
    background: var(--backdrop);
    font-family: "Open Sans", Arial, sans-serif;
    position: relative;
  }
  .card {
    position: absolute;
    left: 240px;
    width: 720px;
    height: 410px;
    border-radius: 34px;
    overflow: hidden;
    box-shadow: 0 10px 30px rgba(0,0,0,0.18);
  }
  /* Front */
  .card-front {
    top: 60px;
    background: linear-gradient(135deg, #1d4ba0 0%, var(--brand-blue) 55%, #2457b3 100%);
    display: flex;
    align-items: center;
    justify-content: center;
  }
  .brand-lockup { display: flex; align-items: center; gap: 18px; }
  .brand-square {
    width: 40px; height: 40px;
    background: var(--steel-grey);
  }
  .brand-name {
    font-weight: 600;
    font-size: 44px;
    letter-spacing: -0.5px;
    color: #ffffff;
  }
  /* Back */
  .card-back {
    top: 530px;
    background: var(--paper);
  }
  .back-band { position: absolute; left: 0; top: 0; width: 720px; height: 410px; }
  .back-lockup {
    position: absolute; top: 70px; right: 56px;
    display: flex; align-items: center; gap: 12px;
  }
  .back-lockup .brand-square { width: 24px; height: 24px; background: var(--brand-blue); }
  .back-lockup .brand-name { font-size: 27px; color: var(--brand-blue); }
  .accent-block {
    position: absolute; top: 140px; right: 60px;
    width: 120px; height: 98px;
    background: var(--brand-blue);
    border-radius: 6px;
  }
  .person {
    position: absolute; top: 150px; left: 52px;
    padding-left: 16px;
    border-left: 3px solid var(--brand-blue);
  }
  .person-name { font-size: 27px; font-weight: 600; color: var(--ink); line-height: 1.1; }
  .person-title { font-size: 14px; color: var(--steel-grey); }
  .contact-list {
    position: absolute; top: 228px; left: 70px;
    list-style: none;
    font-size: 14.5px; color: var(--ink);
    line-height: 22px;
  }
  .contact-list li { display: flex; align-items: center; gap: 10px; }
  .contact-list svg { width: 13px; height: 13px; fill: var(--brand-blue); flex: none; }
  .contact-address { margin-top: 6px; }
</style>
</head>
<body>

<section class="card card-front" aria-label="Business card front">
  <div class="brand-lockup">
    <span class="brand-square"></span>
    <span class="brand-name">Brandvale Fabrication</span>
  </div>
</section>

<section class="card card-back" aria-label="Business card back">
  <svg class="back-band" viewBox="0 0 720 410" aria-hidden="true">
    <polygon points="0,396 720,340 720,410 0,410" fill="var(--brand-blue)"/>
  </svg>

  <div class="back-lockup">
    <span class="brand-square"></span>
    <span class="brand-name">Brandvale Fabrication</span>
  </div>

  <div class="accent-block"></div>

  <div class="person">
    <div class="person-name">Peter Walsh</div>
    <div class="person-title">Managing Director</div>
  </div>

  <ul class="contact-list">
    <li>
      <svg viewBox="0 0 16 16"><rect x="1" y="5" width="14" height="9" rx="2"/><rect x="3" y="2" width="10" height="4" rx="2"/></svg>
      1300 418 592
    </li>
    <li>
      <svg viewBox="0 0 16 16"><path d="M3 1l3 0 1 4-2 1c1 2 3 4 5 5l1-2 4 1 0 3c0 1-1 2-2 2C7 15 1 9 1 3c0-1 1-2 2-2z"/></svg>
      0427 385 914
    </li>
    <li>
      <svg viewBox="0 0 16 16"><path d="M1 3h14v10H1z"/><path d="M1 3l7 6 7-6" fill="none" stroke="#fff" stroke-width="1.4"/></svg>
      peter.walsh@brandvalefabrication.com.au
    </li>
    <li>
      <svg viewBox="0 0 16 16"><circle cx="8" cy="8" r="7"/><path d="M1 8h14M8 1c-3 4-3 10 0 14M8 1c3 4 3 10 0 14" fill="none" stroke="#fff" stroke-width="1"/></svg>
      www.brandvalefabrication.com.au
    </li>
    <li class="contact-address">
      <svg viewBox="0 0 16 16"><path d="M8 1L0 8h2v7h4v-4h4v4h4V8h2z"/></svg>
      58 Harlow Lane, Sydney NSW 2000
    </li>
  </ul>
</section>

</body>
</html>
```